Custom Harbor Blinds ( I have a logo)

We need a medium van wrap design (Norvik talora cargo van 2500 regular base 4 doors) for small business. We develop custom windows treatmeants ( blind...

Target Market(s)

Installations and sales of window coverings

Industry/Entity Type

Business

Requirements
Must have
• Clean description of what we do and the slogan of the company ( Your vision, our quality
Nice to have
• Clean and professional look, free consultation , fully insured
Should not have
• To many pictures, we are more interested on customers focusing in what kind of work we perform than looking an a gallery on wheels

```html
<!DOCTYPE html>
<html lang="en">
<head>
<meta charset="utf-8">
<title>Custom Harbor Blinds – Van Wrap Layout</title>
<link rel="stylesheet" href="https://fonts.googleapis.com/css2?family=Montserrat:wght@400;500;600;700&display=swap">
<style>
  :root {
    --canvas-bg: #58585a;
    --wrap-dark: #231f20;
    --wrap-orange: #e8672c;
    --wrap-white: #ffffff;
    --text-gray: #5b5b5d;
    --cut-line: #d8282f;
    --glass: #58585a;
  }
  html, body { margin: 0; padding: 0; overflow: hidden; background: var(--canvas-bg); }
  .canvas { width: 1200px; height: 800px; overflow: hidden; background: var(--canvas-bg); }
  .canvas svg { display: block; width: 1200px; height: 800px; }
  text { font-family: "Montserrat", sans-serif; }
  .body-panel { fill: var(--wrap-white); }
  .outline { fill: none; stroke: var(--cut-line); stroke-width: 1; }
  .dark-field { fill: var(--wrap-dark); }
  .accent-stripe { fill: var(--wrap-orange); }
  .side-band { fill: var(--wrap-dark); }
  .window { fill: var(--glass); stroke: var(--wrap-white); stroke-width: 1; }
  .panel-seam { stroke: var(--cut-line); stroke-width: 0.8; fill: none; }
  .headline { fill: var(--wrap-orange); font-weight: 700; font-size: 26px; }
  .tagline { fill: var(--wrap-white); font-weight: 500; font-size: 8.6px; }
  .service { fill: var(--wrap-white); font-weight: 600; font-size: 8.4px; }
  .bullet { fill: var(--wrap-orange); }
  .brand-mark { fill: var(--wrap-orange); }
  .brand-name { fill: var(--text-gray); font-weight: 600; font-size: 15px; }
  .slogan { fill: var(--wrap-orange); font-weight: 600; font-size: 8.6px; }
  .call-label { fill: var(--text-gray); font-weight: 500; font-size: 9px; }
  .phone { fill: var(--wrap-orange); font-weight: 700; font-size: 19px; }
  .address { fill: var(--text-gray); font-weight: 500; font-size: 6.4px; }
  .arch-photo { fill: url(#archFill); stroke: var(--wrap-orange); stroke-width: 6; }
</style>
</head>
<body>
<div class="canvas">
<svg viewBox="120 225 1290 860" xmlns="http://www.w3.org/2000/svg">
  <defs>
    <linearGradient id="archFill" x1="0" y1="0" x2="0" y2="1">
      <stop offset="0" stop-color="#e8672c"/>
      <stop offset="0.38" stop-color="#c9582a"/>
      <stop offset="0.42" stop-color="#a9a49c"/>
      <stop offset="1" stop-color="#d9d3cb"/>
    </linearGradient>
    <clipPath id="driverSideClip">
      <path d="M160,625 L158,485 Q160,420 180,378 Q185,372 200,372 L690,374 Q720,376 745,395 L830,480 Q900,492 925,500 Q940,510 938,520 L935,560 Q935,595 920,612 L885,614 A48,52 0 0 0 790,616 L388,628 A68,75 0 0 0 252,628 L160,625 Z"/>
    </clipPath>
    <clipPath id="passengerSideClip">
      <path d="M172,830 L168,806 Q175,796 195,790 L262,772 L332,706 Q345,692 368,690 L920,682 Q935,688 938,710 L940,900 Q940,930 928,934 L825,937 A60,70 0 0 0 705,940 L320,930 L300,928 A52,56 0 0 0 200,880 L180,870 Q170,860 172,830 Z"/>
    </clipPath>
  </defs>

  <!-- Driver side -->
  <g class="van-side driver-side">
    <g clip-path="url(#driverSideClip)">
      <rect class="body-panel" x="150" y="365" width="800" height="275"/>
      <polygon class="dark-field" points="150,365 440,365 530,495 632,640 150,640"/>
      <polygon class="accent-stripe" points="440,365 458,365 547,490 652,640 632,640 530,495"/>
      <g role="img" aria-label="Arched window with sunburst shade over a bright living room">
        <path class="arch-photo" d="M157.5,632 L157.5,532.5 A57.5,57.5 0 0 1 272.5,532.5 L272.5,632 Z"/>
      </g>
      <g role="img" aria-label="Arched window with shade and shuttered room interior" transform="rotate(20 333 505)">
        <path class="arch-photo" d="M285.5,555 L285.5,505.5 A47.5,47.5 0 0 1 380.5,505.5 L380.5,555 Z"/>
      </g>
      <g role="img" aria-label="Arched window with sunburst shade over a dining room" transform="rotate(8 458 565)">
        <path class="arch-photo" d="M393,640 L393,555 A65,65 0 0 1 523,555 L523,640 Z"/>
      </g>
    </g>
    <rect class="window" x="425" y="390" width="85" height="95" rx="6"/>
    <rect class="window" x="523" y="390" width="99" height="95" rx="6"/>
    <path class="window" d="M652,400 Q652,392 662,392 L740,392 Q755,394 770,410 L818,478 Q820,487 810,487 L662,487 Q652,487 652,477 Z"/>
    <line class="panel-seam" x1="515" y1="380" x2="515" y2="625"/>
    <line class="panel-seam" x1="637" y1="378" x2="637" y2="622"/>
    <line class="panel-seam" x1="797" y1="490" x2="797" y2="612"/>
    <path class="outline" d="M160,625 L158,485 Q160,420 180,378 Q185,372 200,372 L690,374 Q720,376 745,395 L830,480 Q900,492 925,500 Q940,510 938,520 L935,560 Q935,595 920,612 L885,614 A48,52 0 0 0 790,616 L388,628 A68,75 0 0 0 252,628 L160,625 Z"/>

    <text class="headline" x="207" y="405">SPECIALIZING</text>
    <text class="tagline" x="207" y="416">in USA-made custom home treatments</text>
    <text class="tagline" x="207" y="425">and shades</text>
    <circle class="bullet" cx="212" cy="443" r="3"/><text class="service" x="219" y="446">Business or Residential</text>
    <circle class="bullet" cx="212" cy="454" r="3"/><text class="service" x="219" y="457">Installs</text>
    <circle class="bullet" cx="212" cy="465" r="3"/><text class="service" x="219" y="468">Motors</text>

    <rect class="brand-mark" x="650" y="498" width="40" height="40"/>
    <text class="brand-name" x="700" y="521">CUSTOM</text>
    <text class="brand-name" x="700" y="536">HARBOR</text>
    <text class="brand-name" x="700" y="551">BLINDS</text>
    <text class="slogan" x="647" y="565">Your vision, our quality</text>
    <text class="call-label" x="647" y="579">Call us today</text>
    <text class="phone" x="647" y="596">201-555-0142</text>
    <text class="address" x="647" y="605">28 Pier Lane, Bayview, NJ 07002.</text>
  </g>

  <!-- Passenger side -->
  <g class="van-side passenger-side">
    <g clip-path="url(#passengerSideClip)">
      <rect class="body-panel" x="160" y="675" width="790" height="275"/>
      <polygon class="dark-field" points="668,675 950,675 950,950 478,950 550,805"/>
      <polygon class="accent-stripe" points="650,675 668,675 550,805 478,950 458,950 533,800"/>
      <g role="img" aria-label="Arched window with sunburst shade over a dining area" transform="rotate(-10 630 870)">
        <path class="arch-photo" d="M562.5,950 L562.5,862.5 A67.5,67.5 0 0 1 697.5,862.5 L697.5,950 Z"/>
      </g>
      <g role="img" aria-label="Arched window with shade and shuttered room interior" transform="rotate(15 760 810)">
        <path class="arch-photo" d="M715,860 L715,807 A45,45 0 0 1 805,807 L805,860 Z"/>
      </g>
      <g role="img" aria-label="Arched window with sunburst shade over a bright living room" transform="rotate(10 880 860)">
        <path class="arch-photo" d="M817.5,945 L817.5,842.5 A62.5,62.5 0 0 1 942.5,842.5 L942.5,945 Z"/>
      </g>
    </g>
    <path class="window" d="M275,775 L345,705 Q350,700 360,700 L435,698 Q443,698 443,706 L443,785 Q443,792 435,792 L290,793 Q272,792 275,775 Z"/>
    <line class="panel-seam" x1="458" y1="692" x2="458" y2="930"/>
    <line class="panel-seam" x1="298" y1="795" x2="298" y2="926"/>
    <path class="outline" d="M172,830 L168,806 Q175,796 195,790 L262,772 L332,706 Q345,692 368,690 L920,682 Q935,688 938,710 L940,900 Q940,930 928,934 L825,937 A60,70 0 0 0 705,940 L320,930 L300,928 A52,56 0 0 0 200,880 L180,870 Q170,860 172,830 Z"/>

    <text class="headline" x="684" y="714">SPECIALIZING</text>
    <text class="tagline" x="684" y="725">in USA-made custom home treatments</text>
    <text class="tagline" x="684" y="734">and shades</text>
    <circle class="bullet" cx="689" cy="752" r="3"/><text class="service" x="696" y="755">Business or Residential</text>
    <circle class="bullet" cx="689" cy="763" r="3"/><text class="service" x="696" y="766">Installs</text>
    <circle class="bullet" cx="689" cy="774" r="3"/><text class="service" x="696" y="777">Motors</text>

    <rect class="brand-mark" x="329" y="808" width="40" height="40"/>
    <text class="brand-name" x="380" y="831">CUSTOM</text>
    <text class="brand-name" x="380" y="846">HARBOR</text>
    <text class="brand-name" x="380" y="861">BLINDS</text>
    <text class="slogan" x="328" y="875">Your vision, our quality</text>
    <text class="call-label" x="328" y="889">Call us today</text>
    <text class="phone" x="328" y="906">201-555-0142</text>
    <text class="address" x="328" y="915">28 Pier Lane, Bayview, NJ 07002.</text>
  </g>

  <!-- Rear doors -->
  <g class="van-rear">
    <path class="body-panel" d="M1040,650 L1056,648 Q1060,560 1080,535 Q1090,527 1110,527 L1310,527 Q1330,527 1340,540 Q1358,560 1362,648 L1380,650 L1378,782 L1045,785 Z"/>
    <rect class="side-band" x="1038" y="648" width="20" height="136"/>
    <rect class="side-band" x="1360" y="648" width="20" height="134"/>
    <path class="window" d="M1068,640 Q1066,562 1080,543 Q1088,535 1100,535 L1192,535 Q1200,535 1200,543 L1200,643 Q1200,650 1192,650 L1076,648 Q1068,648 1068,640 Z"/>
    <path class="window" d="M1350,640 Q1352,562 1338,543 Q1330,535 1318,535 L1226,535 Q1218,535 1218,543 L1218,643 Q1218,650 1226,650 L1342,648 Q1350,648 1350,640 Z"/>
    <line class="panel-seam" x1="1209" y1="527" x2="1209" y2="784"/>
    <path class="outline" d="M1040,650 L1056,648 Q1060,560 1080,535 Q1090,527 1110,527 L1310,527 Q1330,527 1340,540 Q1358,560 1362,648 L1380,650 L1378,782 L1045,785 Z"/>

    <rect class="brand-mark" x="1074" y="662" width="40" height="40"/>
    <text class="brand-name" x="1126" y="685">CUSTOM</text>
    <text class="brand-name" x="1126" y="700">HARBOR</text>
    <text class="brand-name" x="1126" y="715">BLINDS</text>
    <text class="slogan" x="1073" y="729">Your vision, our quality</text>
    <text class="call-label" x="1073" y="743">Call us today</text>
    <text class="phone" x="1073" y="760">201-555-0142</text>
    <text class="address" x="1073" y="769">28 Pier Lane, Bayview, NJ 07002.</text>
  </g>
</svg>
</div>
</body>
</html>
```